Need Help having my business card stand out

I am the owner of Pine Ridge Canine Coaching and would like for my business cards to stand out. I have been trying to keep designing them myself but I can't get what I have in my head on the card. I will try my best to post templates that I like for inspirations. I want something unique but elegant. I don't want in to look cartoony or cheesy. It needs to pop in a pet shop but also in a coffee shop or gym.

Target Market(s)

Dog owners, Married ,No young kids Jr High school kids and up (maybe kids on the way) Executives, Stay at home moms/wives, Small business owners

Industry/Entity Type

Dog Training

Contact Information for Business Card

Trevor Holloway, 555-304-7162, info@pineridgecanine.example, www.pineridgecanine.example

Colors

Designer to choose colors to be used in the design.

Requirements
Must have
• my logo
Should not have
• Cursive lettering

```html
<!DOCTYPE html>
<html lang="en">
<head>
<meta charset="utf-8">
<title>Pine Ridge Canine Coaching – Business Card</title>
<link href="https://fonts.googleapis.com/css2?family=Roboto:wght@400;500&display=swap" rel="stylesheet">
<style>
  :root {
    --backdrop: #141414;
    --card-white: #ffffff;
    --ink: #1a1a1a;
    --rule: #c9c9c9;
    --band: #111111;
    --grass-dark: #34432f;
    --grass-mid: #4d5e43;
    --grass-light: #6f7d62;
    --coat-dark: #231b16;
    --coat-tan: #b98a5a;
    --coat-rust: #7a4a26;
    --glow: rgba(236, 239, 240, 0.92);
  }
  * { box-sizing: border-box; margin: 0; padding: 0; }
  html, body {
    width: 1200px; height: 1200px; overflow: hidden;
    background: var(--backdrop);
    font-family: "Roboto", Arial, sans-serif;
  }
  .sheet {
    width: 1200px; height: 1200px;
    display: flex; flex-direction: column; align-items: center; justify-content: center;
    gap: 70px;
  }
  .card {
    position: relative;
    width: 840px; height: 480px;
    overflow: hidden;
    box-shadow: 0 18px 40px rgba(0,0,0,0.55);
  }

  /* Front */
  .card-front {
    background: linear-gradient(165deg, var(--grass-light) 0%, var(--grass-mid) 45%, var(--grass-dark) 100%);
  }
  .card-front .photo {
    position: absolute; left: 400px; top: 0; right: 0; height: 330px;
    background:
      linear-gradient(100deg, var(--coat-dark) 0%, var(--coat-dark) 30%, var(--coat-rust) 42%, var(--coat-tan) 58%, #c99b6b 80%, var(--grass-mid) 100%);
    -webkit-mask-image: linear-gradient(to bottom, #000 70%, transparent 100%);
    mask-image: linear-gradient(to bottom, #000 70%, transparent 100%);
  }
  .card-front .brand-glow {
    position: absolute; left: 30px; top: 150px;
    width: 360px; height: 300px;
    border-radius: 50%;
    background: radial-gradient(ellipse, var(--glow) 0%, rgba(222,226,228,0.7) 45%, transparent 72%);
  }
  .brand {
    position: absolute;
    display: flex; flex-direction: column; align-items: center; gap: 14px;
    text-align: center;
    font-weight: 500; line-height: 1.15;
    color: var(--ink);
  }
  .brand-mark {
    width: 72px; height: 72px; border-radius: 50%;
    border: 5px solid var(--ink);
  }
  .card-front .brand { left: 70px; top: 200px; width: 280px; font-size: 30px; }

  /* Back */
  .card-back { background: var(--card-white); }
  .card-back .brand { left: 40px; top: 90px; width: 260px; font-size: 30px; }
  .card-back .divider {
    position: absolute; left: 330px; top: 60px;
    width: 1px; height: 210px; background: var(--rule);
  }
  .contact {
    position: absolute; left: 365px; top: 66px;
    color: var(--ink);
  }
  .contact .name { font-size: 38px; font-weight: 400; margin-bottom: 20px; }
  .contact ul { list-style: none; }
  .contact li {
    display: flex; align-items: center; gap: 12px;
    font-size: 24px; line-height: 1.6;
  }
  .contact svg { width: 22px; height: 22px; flex: none; }
  .band-upper {
    position: absolute; right: 0; top: 300px;
    width: 300px; height: 34px;
    background: var(--band);
    clip-path: polygon(20px 0, 100% 0, 100% 100%, 0 100%);
  }
  .band-lower {
    position: absolute; left: 0; right: 0; top: 408px; height: 34px;
    background: var(--band);
  }
</style>
</head>
<body>
<main class="sheet">
  <section class="card card-front">
    <div class="photo" role="img" aria-label="Photo of three dogs sitting together on a grassy lawn"></div>
    <div class="brand-glow"></div>
    <div class="brand">
      <span class="brand-mark"></span>
      <span>Pine Ridge Canine Coaching</span>
    </div>
  </section>

  <section class="card card-back">
    <div class="brand">
      <span class="brand-mark"></span>
      <span>Pine Ridge Canine Coaching</span>
    </div>
    <div class="divider"></div>
    <div class="contact">
      <p class="name">Trevor Holloway</p>
      <ul>
        <li>
          <svg viewBox="0 0 24 24" aria-hidden="true"><path fill="#1a1a1a" d="M6.6 10.8a15.1 15.1 0 0 0 6.6 6.6l2.2-2.2c.3-.3.7-.4 1-.2 1.1.4 2.3.6 3.6.6.6 0 1 .4 1 1V20c0 .6-.4 1-1 1A17 17 0 0 1 3 4c0-.6.4-1 1-1h3.5c.6 0 1 .4 1 1 0 1.3.2 2.5.6 3.6.1.3 0 .7-.2 1z"/></svg>
          555-304-7162
        </li>
        <li>
          <svg viewBox="0 0 24 24" aria-hidden="true"><circle cx="12" cy="12" r="9" fill="none" stroke="#1a1a1a" stroke-width="2"/><path d="M3 12h18M12 3c3 3 3 15 0 18M12 3c-3 3-3 15 0 18" fill="none" stroke="#1a1a1a" stroke-width="1.6"/></svg>
          www.pineridgecanine.example
        </li>
        <li>
          <svg viewBox="0 0 24 24" aria-hidden="true"><rect x="2" y="5" width="20" height="14" fill="#1a1a1a"/><path d="M2 5l10 8 10-8" fill="none" stroke="#fff" stroke-width="1.6"/></svg>
          info@pineridgecanine.example
        </li>
      </ul>
    </div>
    <div class="band-upper"></div>
    <div class="band-lower"></div>
  </section>
</main>
</body>
</html>
```